Quillby Systems Business Card

Create an appealing and elegant Business card for quillby systems. Include logo and use related colors from website, be creative. Include Business name, my name, tile, address, contacts, address, and social media contacts if possible. Logo PSD file is attached.

Bleed Area: 3.46" x 2.32"
Trim: 3.3" x 2.16"
Safe Area: 3.14" x 2.02"

Save files as vector-based PDF with outlined text and PNG.
No crop marks
CMYK color setting

Business Card Info:

Quillby Systems

Dorian Vellacott
Owner

418 Bramlow Rd Unit C
Easton Vale, NH 02771
t. 1.888.562.3907
e. dorian.v@quillbysys.example
w. www.quillbysys.example

facebook. www.friendspace.example/QuillbySys
twitter. chirper.example/quillbysys
pinterest. www.pinboard.example/quillbysys/

Target Market(s)

Business Owners and Partners

Industry/Entity Type

Business

Requirements
Must have
• Logo and related colors from website

```html
<!DOCTYPE html>
<html lang="en">
<head>
<meta charset="utf-8">
<title>Quillby Systems – Business Card</title>
<link rel="stylesheet" href="https://fonts.googleapis.com/css2?family=Source+Sans+3:wght@400;600&display=swap">
<style>
  :root {
    --card-top: #a39c8e;
    --card-mid: #8c867a;
    --card-bottom: #6b675e;
    --stripe-light: rgba(255, 255, 255, 0.72);
    --banner-blue: #4a72a8;
    --banner-edge: #ffffff;
    --ink-light: #f3f1ec;
    --logo-navy: #16202e;
    --icon-blue: #4a72a8;
  }
  html, body {
    margin: 0;
    padding: 0;
    width: 1200px;
    height: 787px;
    overflow: hidden;
    background: #ffffff;
  }
  .card {
    position: relative;
    width: 1200px;
    height: 787px;
    overflow: hidden;
    font-family: "Source Sans 3", "Myriad Pro", sans-serif;
    color: var(--ink-light);
    background: radial-gradient(ellipse at 62% 30%, var(--card-top) 0%, var(--card-mid) 45%, var(--card-bottom) 100%);
  }
  .stripe-band {
    position: absolute;
    left: 0;
    top: 0;
    width: 1200px;
    height: 363px;
    background: repeating-linear-gradient(
      to bottom,
      transparent 0px,
      transparent 16px,
      var(--stripe-light) 16px,
      var(--stripe-light) 27px
    );
  }
  .name-banner {
    position: absolute;
    left: 0;
    top: 150px;
    width: 560px;
    height: 160px;
    filter: drop-shadow(0 10px 8px rgba(0, 0, 0, 0.35));
  }
  .holder-name {
    position: absolute;
    left: 61px;
    top: 184px;
    margin: 0;
    font-size: 56px;
    font-weight: 400;
    line-height: 1;
    letter-spacing: 0.2px;
    white-space: nowrap;
  }
  .holder-title {
    position: absolute;
    left: 61px;
    top: 235px;
    margin: 0;
    font-size: 40px;
    font-weight: 400;
    line-height: 1;
  }
  .brand-name {
    position: absolute;
    left: 640px;
    top: 128px;
    width: 500px;
    margin: 0;
    font-size: 82px;
    font-weight: 600;
    line-height: 0.98;
    color: var(--logo-navy);
    text-align: center;
  }
  .contact-block {
    position: absolute;
    left: 85px;
    top: 512px;
    margin: 0;
    font-size: 32px;
    line-height: 41px;
    font-style: normal;
    white-space: nowrap;
  }
  .mail-icon {
    position: absolute;
    left: 36px;
    top: 509px;
    width: 42px;
    height: 42px;
  }
  .social-list {
    position: absolute;
    left: 591px;
    top: 508px;
    margin: 0;
    padding: 0;
    list-style: none;
  }
  .social-item {
    display: flex;
    align-items: center;
    height: 44px;
    margin-bottom: 35px;
    font-size: 31px;
    white-space: nowrap;
  }
  .social-dot {
    width: 42px;
    height: 42px;
    border-radius: 50%;
    background: var(--icon-blue);
    margin-right: 9px;
    flex: none;
  }
</style>
</head>
<body>
<main class="card">
  <div class="stripe-band"></div>

  <svg class="name-banner" viewBox="0 0 560 160" aria-hidden="true">
    <polygon points="0,4 548,4 438,152 0,152" fill="var(--banner-edge)"/>
    <polygon points="0,12 532,12 432,144 0,144" fill="var(--banner-blue)"/>
  </svg>
  <h1 class="holder-name">Dorian Vellacott</h1>
  <p class="holder-title">Owner</p>

  <p class="brand-name">Quillby<br>Systems</p>

  <svg class="mail-icon" viewBox="0 0 42 42" aria-hidden="true">
    <circle cx="21" cy="21" r="21" fill="var(--icon-blue)"/>
    <rect x="11" y="14" width="20" height="14" rx="1.5" fill="#ffffff"/>
    <polyline points="11.5,15 21,22.5 30.5,15" fill="none" stroke="var(--icon-blue)" stroke-width="2"/>
  </svg>
  <address class="contact-block">
    418 Bramlow Rd Unit C<br>
    Easton Vale, NH 02771<br>
    t. 1.888.562.3907<br>
    e. dorian.v@quillbysys.example<br>
    w. www.quillbysys.example
  </address>

  <ul class="social-list">
    <li class="social-item"><span class="social-dot"></span>www.friendspace.example/QuillbySys</li>
    <li class="social-item"><span class="social-dot"></span>chirper.example/quillbysys</li>
    <li class="social-item"><span class="social-dot"></span>www.pinboard.example/quillbysys/</li>
  </ul>
</main>
</body>
</html>
```